Sci fi cover needed for Brimbly/aMolder

I'd like a variation on the below design, I like the white logo with the colour blending in but this time with a different colour and different graphic below. No subtitle needed.

```html
<!DOCTYPE html>
<html lang="en">
<head>
<meta charset="utf-8">
<title>Farther Orbitstations — Cover</title>
<link rel="stylesheet" href="https://fonts.googleapis.com/css2?family=Black+Ops+One&display=swap">
<style>
  :root {
    --space-top: #030202;
    --space-mid: #1a100c;
    --space-low: #2e1c14;
    --gold-pale: #fbf3d6;
    --gold-bright: #f6ea7a;
    --gold-deep: #e9a83c;
    --ember: #d0401c;
    --ember-dark: #6e1f12;
    --flame: #f7a21e;
    --glow-core: #ffe58a;
    --glow-edge: #c06a10;
  }
  html, body {
    margin: 0;
    padding: 0;
    width: 1200px;
    height: 1200px;
    overflow: hidden;
    background: var(--space-top);
  }
  .cover {
    position: relative;
    width: 1200px;
    height: 1200px;
    background: linear-gradient(180deg, var(--space-top) 0%, var(--space-mid) 55%, var(--space-low) 100%);
    overflow: hidden;
  }
  .cover__art {
    position: absolute;
    inset: 0;
    width: 1200px;
    height: 1200px;
  }
  .title {
    font-family: "Black Ops One", "Impact", sans-serif;
  }
</style>
</head>
<body>
<main class="cover">
  <svg class="cover__art" viewBox="0 0 1200 1200" xmlns="http://www.w3.org/2000/svg">
    <defs>
      <linearGradient id="title-gold" x1="0" y1="0" x2="1" y2="1">
        <stop offset="0" stop-color="var(--gold-bright)"/>
        <stop offset="0.45" stop-color="var(--gold-bright)"/>
        <stop offset="0.75" stop-color="var(--gold-deep)"/>
        <stop offset="1" stop-color="var(--gold-pale)"/>
      </linearGradient>
      <linearGradient id="title-gold-right" x1="0" y1="0" x2="1" y2="0">
        <stop offset="0" stop-color="var(--gold-bright)"/>
        <stop offset="0.6" stop-color="var(--gold-bright)"/>
        <stop offset="1" stop-color="var(--gold-pale)"/>
      </linearGradient>
      <radialGradient id="energy-glow" cx="0.5" cy="0.55" r="0.5">
        <stop offset="0" stop-color="var(--glow-core)" stop-opacity="0.55"/>
        <stop offset="0.5" stop-color="var(--flame)" stop-opacity="0.45"/>
        <stop offset="0.8" stop-color="var(--glow-edge)" stop-opacity="0.25"/>
        <stop offset="1" stop-color="var(--glow-edge)" stop-opacity="0"/>
      </radialGradient>
      <linearGradient id="wave-back" x1="0" y1="0" x2="1" y2="0">
        <stop offset="0" stop-color="var(--ember-dark)"/>
        <stop offset="1" stop-color="#8a2a18"/>
      </linearGradient>
      <linearGradient id="wave-front" x1="0" y1="0" x2="1" y2="0">
        <stop offset="0" stop-color="var(--flame)"/>
        <stop offset="0.35" stop-color="var(--ember)"/>
        <stop offset="0.7" stop-color="#e0501e"/>
        <stop offset="1" stop-color="var(--flame)"/>
      </linearGradient>
    </defs>

    <!-- title -->
    <text class="title" x="199" y="256" textLength="825" lengthAdjust="spacingAndGlyphs"
          font-size="288" fill="url(#title-gold)">FARTHER</text>
    <text class="title" x="199" y="367" textLength="825" lengthAdjust="spacingAndGlyphs"
          font-size="139" fill="url(#title-gold-right)">ORBITSTATIONS</text>

    <!-- lower horizon bands -->
    <path class="horizon horizon--back"
          d="M0 1010 C 250 1100, 520 1130, 760 1100 C 960 1075, 1100 1000, 1200 950 L1200 1200 L0 1200 Z"
          fill="url(#wave-back)" opacity="0.75"/>
    <path class="horizon horizon--front"
          d="M0 1128 C 200 1170, 420 1200, 600 1200 L0 1200 Z"
          fill="url(#wave-front)"/>
    <path class="horizon horizon--front"
          d="M560 1200 C 800 1170, 1050 1130, 1200 1058 L1200 1200 Z"
          fill="url(#wave-front)"/>
    <path class="horizon horizon--mid"
          d="M0 1090 C 300 1150, 640 1160, 900 1120 C 1040 1098, 1130 1070, 1200 1040 L1200 1080 C 1080 1130, 900 1170, 620 1175 C 380 1178, 160 1140, 0 1110 Z"
          fill="var(--ember)" opacity="0.35"/>

    <!-- energy swirl artwork area -->
    <ellipse class="energy-swirl" role="img" aria-label="Glowing golden energy rings swirling above the planet horizon"
             cx="603" cy="880" rx="500" ry="200" fill="url(#energy-glow)"/>
  </svg>
</main>
</body>
</html>
```